BrookvaleLogic Website Design

To design a website for BrookvaleLogic, a software development company. The website should reflect the branding of our company, which is Smart, Beautiful, and Sophisticated. The existing website is www.brookvalelogic-example.com.sg

```html
<!DOCTYPE html>
<html lang="en">
<head>
<meta charset="utf-8">
<title>BrookvaleLogic — Software Development</title>
<link href="https://fonts.googleapis.com/css2?family=Lato:wght@300;400;700;900&display=swap" rel="stylesheet">
<style>
:root{
  --navy:#1d4f82;
  --slate:#2f3a4c;
  --ink:#333a44;
  --muted:#7a8088;
  --light:#eef0f2;
  --accent:#2a8bcb;
  --orange:#f26a10;
  --white:#ffffff;
  --footer:#1e1f22;
  --footer-deep:#141517;
}
*{margin:0;padding:0;box-sizing:border-box}
html,body{width:1200px;height:3731px;overflow:hidden}
body{font-family:"Lato",Arial,sans-serif;color:var(--ink);background:var(--white);position:relative}
section,header,footer,nav{position:relative;width:1200px;overflow:hidden}
.abs{position:absolute}
.btn{display:inline-block;font-size:13px;font-weight:700;padding:9px 18px;border-radius:2px;color:var(--white)}
.btn-orange{background:var(--orange)}
.btn-outline{border:1px solid var(--white)}
.btn-blue{background:var(--accent)}

.site-header{height:87px;background:var(--white)}
.brand{left:160px;top:20px;display:flex;align-items:center;gap:10px}
.brand-dot{width:44px;height:44px;border-radius:50%;background:var(--navy)}
.brand-name{font-size:30px;font-weight:700;color:var(--navy)}
.contact{top:24px;display:flex;align-items:center;gap:10px;font-size:13px;color:var(--ink);line-height:1.3}
.contact .ico{width:30px;height:30px;border-radius:50%;background:var(--navy);display:flex;align-items:center;justify-content:center}
.contact b{color:var(--muted);font-weight:400;display:block}
.main-nav{height:31px;background:var(--navy);display:flex;align-items:center;padding-left:165px}
.main-nav a{color:var(--white);font-size:14px;font-weight:700;margin-right:54px;text-decoration:none}
.chat{position:absolute;right:155px;top:7px;color:var(--white);font-size:14px;font-weight:700;display:flex;gap:8px;align-items:center}

.hero{height:467px;background:linear-gradient(90deg,#5e6366 0%,#a9adaf 40%,#d4d6d6 70%,#8e9294 100%)}
.hero-bg{inset:0;background:linear-gradient(180deg,rgba(40,44,48,.35),rgba(40,44,48,.15))}
.hero-copy{left:162px;top:108px;color:var(--white);width:300px}
.hero-copy h1{font-weight:300;font-size:32px;line-height:1.1}
.hero-copy h1 strong{font-weight:900;display:block}
.hero-copy p{font-size:12px;line-height:1.45;margin:14px 0 18px}
.hero-screen{left:575px;top:52px;width:467px;height:340px}
.hero-strip{left:0;bottom:0;width:100%;height:50px;background:rgba(30,34,40,.85);color:var(--white);font-size:14px;padding:17px 0 0 162px}

.clients{height:83px;background:var(--light);display:flex;align-items:center;padding-left:180px;gap:76px}
.clients .count{font-size:14px;color:var(--muted);line-height:1.2}
.clients .count b{color:var(--ink)}
.client-name{font-size:22px;font-weight:700;color:#777c82;letter-spacing:1px}

.welcome{height:420px;text-align:center}
.section-title{font-size:30px;font-weight:300;color:var(--ink)}
.section-title span{color:var(--accent)}
.lede{font-size:12px;color:var(--muted);width:540px;margin:10px auto 0;line-height:1.5}
.services{display:flex;justify-content:center;gap:48px;margin-top:50px}
.service{width:180px}
.service .ring{width:96px;height:96px;border-radius:50%;margin:0 auto;display:flex;align-items:center;justify-content:center;box-shadow:0 0 0 5px #e4e7ea}
.service h3{font-size:15px;font-weight:700;margin:22px 0 6px}
.service p{font-size:12px;color:var(--muted);line-height:1.5}

.discover{height:454px;background:var(--slate);color:var(--white)}
.discover .section-title{color:var(--white);text-align:center;padding-top:22px}
.discover .lede{color:#b6bcc6;text-align:center}
.laptop{left:210px;top:148px;width:330px;height:200px}
.discover-copy{left:585px;top:148px;width:405px}
.discover-copy h2{font-size:18px;font-weight:700}
.discover-copy .strong{font-size:13px;font-weight:700;line-height:1.45;margin:10px 0}
.discover-copy .small{font-size:11px;color:#aab1bc;line-height:1.55}
.discover-actions{margin-top:26px;display:flex;gap:12px}

.works{height:815px;text-align:center}
.works .section-title{padding-top:68px}
.filters{display:flex;justify-content:center;gap:16px;font-size:12px;margin-top:14px;align-items:center}
.filters .on{background:var(--orange);color:var(--white);padding:3px 8px}
.works-grid{position:absolute;left:150px;top:172px;width:892px;height:627px;display:grid;grid-template-columns:1fr 1fr 1fr;gap:2px}
.col{display:flex;flex-direction:column;gap:2px}
.tile{flex:1}
.tile-hover{position:relative;background:#46627e;color:var(--white)}
.tile-hover .cap{position:absolute;left:0;right:0;top:72px;font-size:13px;line-height:1.4}
.tile-hover .acts{position:absolute;left:50%;top:120px;transform:translateX(-50%);display:flex}
.tile-hover .acts span{width:38px;height:38px;display:flex;align-items:center;justify-content:center}

.trusted{height:405px;background:var(--slate);color:var(--white);text-align:center}
.trusted .section-title{color:var(--white);padding-top:50px}
.avatars{display:flex;justify-content:center;gap:10px;margin-top:34px}
.avatars div{width:62px;height:62px;background:linear-gradient(160deg,#9aa0a6,#5c6168)}
.quote{width:780px;margin:30px auto 0;font-size:13px;line-height:1.55}
.author{margin-top:18px;font-size:14px}
.author span{display:block;color:var(--accent)}
.dots{display:flex;justify-content:center;gap:6px;margin-top:12px}
.dots i{width:8px;height:8px;border-radius:50%;background:#7f8795}
.dots i.on{background:var(--white)}

.social{height:528px;text-align:center}
.social .section-title{padding-top:50px}
.social-row{display:flex;justify-content:center;gap:30px;margin-top:44px}
.social-row div{width:84px;height:84px;border-radius:50%;color:var(--white);font-size:16px;font-weight:700;display:flex;align-items:center;justify-content:center}
.social-pointer{display:block;margin:10px 0 0 592px}
.tweet{width:620px;margin:40px auto 0;font-size:13px;line-height:1.5;text-align:left}

.help{height:87px;background:var(--footer);color:var(--white);display:flex;align-items:center;padding:0 160px}
.help p{font-size:18px}
.help .phone{margin-left:auto;font-size:30px;display:flex;align-items:center;gap:10px}
.footer-links{height:286px;background:var(--footer-deep);color:var(--white);display:flex;padding:45px 0 0 148px}
.footer-col{width:230px}
.footer-col h4{font-size:14px;font-weight:700;margin-bottom:12px}
.footer-col ul{list-style:none;font-size:12px;color:#b8bcc2;line-height:1.75}
.footer-col li::before{content:"• ";color:#777}
.footer-col li.on{color:var(--accent)}
.signup p{font-size:11px;color:#b8bcc2;line-height:1.5;width:200px}
.signup .field{width:200px;height:26px;background:#2b2d31;border:1px solid #3a3c41;margin-top:10px;font-size:11px;color:#888;padding:6px}
.signup .btn{margin-top:8px;padding:6px 18px}
.stay{display:flex;gap:6px;margin-top:6px}
.stay i{width:20px;height:20px;background:#3b3e44;border-radius:2px}
.bottom-bar{height:47px;background:var(--footer);color:#8c9096;font-size:12px;display:flex;align-items:center;padding:0 160px}
.bottom-bar nav{width:auto;margin-left:auto;display:flex;gap:14px}
</style>
</head>
<body>

<header class="site-header">
  <div class="brand abs"><div class="brand-dot"></div><span class="brand-name">BrookvaleLogic</span></div>
  <div class="contact abs" style="left:650px">
    <span class="ico"><svg width="14" height="14" viewBox="0 0 24 24"><path fill="#fff" d="M6.6 10.8a15 15 0 006.6 6.6l2.2-2.2c.3-.3.7-.4 1-.2 1.1.4 2.3.6 3.6.6.6 0 1 .4 1 1V20c0 .6-.4 1-1 1A17 17 0 013 4c0-.6.4-1 1-1h3.5c.6 0 1 .4 1 1 0 1.3.2 2.5.6 3.6.1.3 0 .7-.2 1z"/></svg></span>
    <div><b>Questions?</b>Call 1-800-555-0142</div>
  </div>
  <div class="contact abs" style="left:880px">
    <span class="ico"><svg width="14" height="14" viewBox="0 0 24 24"><path fill="#fff" d="M3 5h18v14H3z"/><path d="M3 5l9 7 9-7" stroke="#1d4f82" stroke-width="2" fill="none"/></svg></span>
    <div><b>Email Us</b>info@brookvalelogic.com</div>
  </div>
</header>
<nav class="main-nav">
  <a>Home</a><a>Services</a><a>About Us</a><a>Portfolio</a><a>Contact</a>
  <span class="chat"><svg width="20" height="16" viewBox="0 0 20 16"><path fill="#fff" d="M2 1h12v8H6l-4 3z"/><path fill="#fff" opacity=".7" d="M15 4h3v8l-3-2H8v-1h7z"/></svg>Chat with us now</span>
</nav>

<section class="hero">
  <div class="hero-bg abs" role="img" aria-label="Blurred photograph of a bright modern office"></div>
  <div class="hero-copy abs">
    <h1>We provide you<strong>the best solution</strong>for your business</h1>
    <p>Lorem ipsum dolor sit amet, consectetur adipiscing elit. Aenean commodo ligula eget dolor. Aenean massa. Cum sociis natoque penatibus et magnis dis parturient.</p>
    <span class="btn btn-orange">Request a quote</span>
  </div>
  <div class="hero-screen abs" role="img" aria-label="Desktop monitor showing a sports retail website" style="background:linear-gradient(180deg,#1b1d20,#3b3f45);border-radius:8px"></div>
  <div class="hero-strip abs">Let us handle the <b>technology</b>, so you can focus on your <b>business</b></div>
</section>

<section class="clients">
  <div class="count">Over <b>200</b> happy<br>customers we'd<br>like you to meet</div>
  <span class="client-name">Harbrook</span>
  <span class="client-name">Quillon</span>
  <span class="client-name">Ternfield</span>
  <span class="client-name">Pellmark</span>
</section>

<section class="welcome">
  <h2 class="section-title" style="padding-top:42px">Welcome to <span>BrookvaleLogic Agency</span></h2>
  <p class="lede">Lorem ipsum dolor sit amet, consectetur adipiscing elit. Aenean commodo ligula eget dolor. Aenean massa. Cum sociis natoque penatibus et magnis dis parturient montes, nascetur ridiculus mus. Donec quam felis, ultricies nec, pellentesque eu, pretium quis, sem.</p>
  <div class="services">
    <div class="service">
      <div class="ring" style="background:var(--orange)"><svg width="40" height="40" viewBox="0 0 40 40"><circle cx="20" cy="20" r="12" fill="none" stroke="#fff" stroke-width="3"/><circle cx="20" cy="20" r="4" fill="#fff"/></svg></div>
      <h3 style="color:var(--orange)">Strategy &amp; Consulting</h3>
      <p>Online Business Consulting<br>Website Planning<br>Online Marketing Strategy</p>
    </div>
    <div class="service">
      <div class="ring" style="background:var(--navy)"><svg width="40" height="40" viewBox="0 0 40 40"><path d="M8 8v24h24" stroke="#fff" stroke-width="3" fill="none"/><path d="M12 26l7-8 5 5 8-10" stroke="#fff" stroke-width="3" fill="none"/></svg></div>
      <h3>Online Marketing</h3>
      <p>Search Engine Optimization<br>PPC Marketing<br>Conversion Rate Optimization</p>
    </div>
    <div class="service">
      <div class="ring" style="background:var(--navy)"><svg width="40" height="40" viewBox="0 0 40 40"><path d="M10 30l20-20M10 10l20 20" stroke="#fff" stroke-width="4"/></svg></div>
      <h3>Design &amp; Development</h3>
      <p>Logo &amp; Branding<br>Website Development<br>Ecommerce Websites</p>
    </div>
    <div class="service">
      <div class="ring" style="background:var(--navy)"><svg width="40" height="40" viewBox="0 0 40 40"><rect x="12" y="6" width="16" height="28" rx="3" fill="none" stroke="#fff" stroke-width="3"/><circle cx="20" cy="29" r="1.6" fill="#fff"/></svg></div>
      <h3>Mobile Development</h3>
      <p>Mobile App Development<br>Responsive Website Design<br>Mobile Website Design</p>
    </div>
  </div>
</section>

<section class="discover">
  <h2 class="section-title">Discover more about our solutions</h2>
  <p class="lede">Lorem ipsum dolor sit amet, consectetur adipiscing elit. Aenean commodo ligula eget dolor. Aenean massa. Cum sociis natoque penatibus et magnis dis parturient montes, nasc.</p>
  <div class="laptop abs" role="img" aria-label="Laptop showing a colourful website design" style="background:linear-gradient(180deg,#d9dcdf 0%,#8b9096 88%,#c9ccd0 100%);border-radius:6px"></div>
  <div class="discover-copy abs">
    <h2>We are a group of IT specialists lorem ipsum dolor</h2>
    <p class="strong">Lorem ipsum dolor sit amet, consectetur adipiscing elit. Aenean commodo ligula eget dolor. Aenean massa. Cum sociis natoque penatibus et magnis dis parturient montes, nasc.</p>
    <p class="small">Nam pellentesque id arcu. Duis ut libero, vestibulum eget, imperdiet quis lectus. Sed aliquam ultrices mauris. Integer ante arcu, accumsan a, consectetuer eget, posuere ut, mauris. Praesent adipiscing. Phasellus ullamcorper ipsum rutrum nunc. Nunc nonummy metus. Vestibulum volutpat pretium libero. Cras id dui. Aenean ut eros et nisl sagittis vestibulum. Nullam nulla eros, ultricies sit amet, nonummy id, imperdiet feugiat, pede. Sed lectus.</p>
    <div class="discover-actions"><span class="btn btn-outline">Learn More</span><span class="btn btn-orange">Request a quote</span></div>
  </div>
</section>

<section class="works">
  <h2 class="section-title">Featured works</h2>
  <div class="filters"><span class="on">All</span><span>APP</span><span>Ecommerce</span><span>Charity</span><span>Events</span></div>
  <div class="works-grid">
    <div class="col">
      <div class="tile" role="img" aria-label="Athlete campaign website with yellow layout" style="background:linear-gradient(160deg,#2e2f28,#6e7a2a 60%,#1f2e1c)"></div>
      <div class="tile" role="img" aria-label="Product page with a gold sneaker" style="background:linear-gradient(160deg,#d6c07a,#9d7c2d 60%,#2a2a26)"></div>
    </div>
    <div class="col">
      <div class="tile" role="img" aria-label="Dark sports team website" style="background:linear-gradient(160deg,#151a24,#32415a);flex:.9"></div>
      <div class="tile tile-hover" style="flex:1.1" role="img" aria-label="Photography portfolio website">
        <div class="cap">Photography<br>135: PRINTS, WEB DESIGN</div>
        <div class="acts">
          <span style="background:var(--orange)"><svg width="16" height="16" viewBox="0 0 16 16"><circle cx="6.5" cy="6.5" r="4.5" fill="none" stroke="#fff" stroke-width="2"/><path d="M10 10l4 4" stroke="#fff" stroke-width="2"/></svg></span>
          <span style="background:#fff"><svg width="16" height="16" viewBox="0 0 16 16"><path d="M6 10l4-4M5 7l-2 2a2.5 2.5 0 003.5 3.5l2-2M11 9l2-2a2.5 2.5 0 00-3.5-3.5l-2 2" stroke="#333" stroke-width="1.6" fill="none"/></svg></span>
        </div>
      </div>
      <div class="tile" role="img" aria-label="Watch store website" style="background:linear-gradient(160deg,#2a2c30,#6a6e75);flex:.8"></div>
    </div>
    <div class="col">
      <div class="tile" role="img" aria-label="Sports shoe retail website" style="background:linear-gradient(160deg,#15161a,#4c4f56)"></div>
      <div class="tile" role="img" aria-label="Fashion shop website" style="background:linear-gradient(160deg,#f4f1ee,#d9b9a8)"></div>
      <div class="tile" role="img" aria-label="Green drinks brand website" style="background:linear-gradient(160deg,#3fa72e,#a7d93a)"></div>
    </div>
  </div>
</section>

<section class="trusted">
  <h2 class="section-title">Trusted by more than thousand clinets lorem ipsum</h2>
  <div class="avatars" role="img" aria-label="Portrait photos of five clients">
    <div></div><div></div><div></div><div></div><div></div>
  </div>
  <p class="quote">Lorem ipsum dolor sit amet, consectetur adipiscing elit. Aenean commodo ligula eget dolor. Aenean massa. Cum sociis natoque penatibus et magnis dis parturient montes, nascetur ridiculus mus. Donec quam felis, ultricies nec, pellentesque eu, pretium quis, sem. Nulla consequat massa quis enim. Donec pede justo, fringilla vel, aliquet nec, vulputate eget, arcu. In enim justo</p>
  <p class="author">– Marlen Dovic<span>Studio Northwell</span></p>
  <div class="dots"><i class="on"></i><i></i><i></i><i></i></div>
</section>

<section class="social">
  <h2 class="section-title">We Are Social</h2>
  <div class="social-row">
    <div style="background:#3a5a98">Page</div>
    <div style="background:#2a9fd8">Feed</div>
    <div style="background:#d8432f">Plus</div>
  </div>
  <svg class="social-pointer" width="16" height="10" viewBox="0 0 16 10"><path d="M0 0h16L8 10z" fill="#2a9fd8"/></svg>
  <p class="tweet"><b>http://bit.ly/bvlx01 @Jane Field:</b> Lorem ipsum dolor sit amet, consectetur adipiscing elit. Aenean commodo ligula eget dolor. Aenean massa. Cum sociis natoque penatibus et magnis dis</p>
  <span class="btn btn-blue" style="margin-top:34px">FOLLOW US</span>
</section>

<footer>
  <div class="help">
    <p><b>Need Help?</b> Call Us, Monday to Friday, 10 AM to 6PM</p>
    <span class="phone"><svg width="26" height="26" viewBox="0 0 24 24"><path fill="#fff" d="M6.6 10.8a15 15 0 006.6 6.6l2.2-2.2c.3-.3.7-.4 1-.2 1.1.4 2.3.6 3.6.6.6 0 1 .4 1 1V20c0 .6-.4 1-1 1A17 17 0 013 4c0-.6.4-1 1-1h3.5c.6 0 1 .4 1 1 0 1.3.2 2.5.6 3.6.1.3 0 .7-.2 1z"/></svg>01.46.55.20.13</span>
  </div>
  <div class="footer-links">
    <div class="footer-col"><h4>Services</h4>
      <ul><li>Online Stores</li><li>Social Media</li><li>Online Marketing</li><li class="on">Digital Strategy</li><li>Responsive / Mobile Designs</li><li>Hosting &amp; Domain Registration</li></ul></div>
    <div class="footer-col"><h4>Online Marketing</h4>
      <ul><li>Email Marketing</li><li>Search Engine Optimization</li><li>Paid Search Management</li></ul>
      <h4 style="margin-top:12px">Web Development</h4>
      <ul><li>Web Design</li><li>Content Management Systems</li><li>Web Application Development</li></ul></div>
    <div class="footer-col"><h4>About Us</h4>
      <ul><li>Our Team</li><li>Careers</li><li>Affiliate</li><li>News</li><li>Blog</li><li>Testimonials</li></ul></div>
    <div class="footer-col signup"><h4>Newsletter Signup</h4>
      <p>Sign up for our daily email by entering your information below</p>
      <div class="field">email address</div>
      <span class="btn btn-orange">SUBMIT</span>
      <h4 style="margin-top:16px;margin-bottom:4px">Stay Connected</h4>
      <div class="stay"><i></i><i></i><i></i><i></i><i></i></div>
    </div>
  </div>
  <div class="bottom-bar">Copyright © 2014
    <nav><span>Home</span><span>Services</span><span>Portfolio</span><span>About Us</span><span>Blog</span><span>Contact</span></nav>
  </div>
</footer>

</body>
</html>
```